Technology Solutions Provider

Let’s design a business card that will be as simple and bold at the same time. Name, email address, website & phone number.

Target Market(s)

Small to Medium Size Business

Industry/Entity Type

It Professional

Contact Information for Business Card

Name, email, website, phone numbers

Font styles to use
Sans Serif

Colors
ec1f27
f04a50
dddddd
919191
000000
ffffff

Requirements
Must have
• Clean simple look using my existing logo. I just need to the basic contact information on this card.
Nice to have
• Im considering the square size card versus the standard size business card.
Should not have
• No Mailing Address, no list of services.

```html
<!DOCTYPE html>
<html lang="en">
<head>
<meta charset="utf-8">
<title>Corelink Business Card</title>
<link href="https://fonts.googleapis.com/css2?family=Exo+2:wght@500&family=Lato:wght@400;700&display=swap" rel="stylesheet">
<style>
  :root {
    --red: #ec1f27;
    --red-soft: #f04a50;
    --light: #dddddd;
    --grey: #919191;
    --black: #000000;
    --white: #ffffff;
    --card: #f4f4f4;
  }
  html, body {
    margin: 0;
    width: 1200px;
    height: 970px;
    overflow: hidden;
    background: var(--light);
  }
  .card {
    position: absolute;
    left: 100px;
    top: 201px;
    width: 1000px;
    height: 567px;
    border-radius: 34px;
    background: var(--card);
    box-shadow: 0 2px 10px rgba(0,0,0,0.08);
    font-family: "Lato", sans-serif;
  }
  .brand {
    position: absolute;
    left: 68px;
    top: 250px;
  }
  .brand-name {
    display: flex;
    align-items: center;
    gap: 10px;
    font-family: "Lato", sans-serif;
    font-weight: 700;
    font-size: 54px;
    line-height: 1;
    color: var(--red);
    letter-spacing: 1px;
  }
  .brand-dot {
    width: 16px;
    height: 16px;
    border-radius: 50%;
    background: var(--red);
  }
  .brand-tagline {
    margin-top: 6px;
    font-size: 19px;
    color: var(--grey);
    letter-spacing: 0.5px;
  }
  .divider {
    position: absolute;
    left: 526px;
    top: 196px;
    width: 2px;
    height: 184px;
    background: var(--red);
  }
  .contact {
    position: absolute;
    left: 573px;
    top: 190px;
  }
  .person-name {
    font-family: "Exo 2", sans-serif;
    font-weight: 500;
    font-size: 36px;
    color: var(--black);
    line-height: 1.1;
    letter-spacing: 0.5px;
  }
  .person-role {
    font-family: "Exo 2", sans-serif;
    font-weight: 500;
    font-size: 26px;
    color: var(--red);
    line-height: 1.1;
  }
  .details {
    list-style: none;
    margin: 34px 0 0;
    padding: 0;
  }
  .details li {
    display: flex;
    align-items: center;
    gap: 12px;
    height: 34px;
    font-size: 27px;
    color: var(--black);
  }
  .details svg {
    width: 30px;
    height: 30px;
    flex: none;
  }
</style>
</head>
<body>
  <div class="card">
    <div class="brand">
      <div class="brand-name"><span>corelink</span><span class="brand-dot"></span></div>
      <div class="brand-tagline">technology solutions provider</div>
    </div>

    <div class="divider"></div>

    <div class="contact">
      <div class="person-name">Daniel Reyes</div>
      <div class="person-role">Founder</div>
      <ul class="details">
        <li>
          <svg viewBox="0 0 30 30" aria-hidden="true">
            <circle cx="15" cy="15" r="13" fill="none" stroke="var(--red)" stroke-width="2.5"/>
            <path d="M9 12c0-2 2-3 6-3s6 1 6 3l-2 1-1-2h-6l-1 2zM10 15h10v6h-10z" fill="var(--red)"/>
          </svg>
          <span>(555) 014-2280</span>
        </li>
        <li>
          <svg viewBox="0 0 30 30" aria-hidden="true">
            <circle cx="15" cy="15" r="13" fill="none" stroke="var(--red)" stroke-width="2.5"/>
            <rect x="8" y="10" width="14" height="10" fill="var(--red)"/>
            <path d="M8 10l7 6 7-6M8 20l5-5M22 20l-5-5" fill="none" stroke="var(--white)" stroke-width="1.2"/>
          </svg>
          <span>hello@corelinktech.com</span>
        </li>
        <li>
          <svg viewBox="0 0 30 30" aria-hidden="true">
            <circle cx="15" cy="15" r="13" fill="none" stroke="var(--red)" stroke-width="2.5"/>
            <circle cx="15" cy="15" r="8" fill="var(--red)"/>
            <path d="M7 15h16M15 7v16M15 7c-4 4-4 12 0 16M15 7c4 4 4 12 0 16" fill="none" stroke="var(--white)" stroke-width="1"/>
          </svg>
          <span>www.corelinktech.com</span>
        </li>
      </ul>
    </div>
  </div>
</body>
</html>
```